A Speech Therapy Business needs to update their logo

I need an update to the font and color of my logo to look more appealing. I am looking to open a private practice as a Speech Language Pathologist that caters to adults and children. It needs to be sophisticated and friendly at the same time. I want to keep the silhouette in my logo as is, just update the font and color for "Brightpaths".
Industry/Entity Type
Business
Contact Information for Business Card
I want the business card to have my logo, my name (Dorota Valk, CCC-SLP, TSSLD) and that I am a Bilingual Speech Language Pathologist. Also, include my phone number, (555) 271-8390. Include my website, Brightpathsslp.example, and email address, dorotavalk@brightpathsslp.example
Look and feel
Each slider illustrates characteristics of the customer's brand and the style your logo design should communicate.

```html
<!DOCTYPE html>
<html lang="en">
<head>
<meta charset="utf-8">
<title>Brightpaths Business Card</title>
<link rel="stylesheet" href="https://fonts.googleapis.com/css2?family=Open+Sans:wght@400;600&display=swap">
<style>
  :root {
    --page: #ecebee;
    --card-white: #ffffff;
    --ink: #1a1a1a;
    --black: #0d0d0d;
    --purple: #7b5fb0;
    --purple-light: #b3a0d8;
    --grey: #555555;
    --figure-dark: #2a2a2a;
    --figure-light: #9a9a9a;
  }
  * { box-sizing: border-box; margin: 0; padding: 0; }
  html, body { width: 1200px; height: 950px; overflow: hidden; }
  body {
    background: var(--page);
    font-family: "Open Sans", Arial, sans-serif;
    position: relative;
  }
  .card {
    position: absolute;
    left: 250px;
    width: 700px;
    height: 400px;
    overflow: hidden;
    box-shadow: 0 6px 18px rgba(0,0,0,0.18);
  }
  .card-front { top: 50px; background: var(--card-white); }
  .card-back { top: 500px; background: var(--black); }

  .front-swoosh { position: absolute; inset: 0; width: 700px; height: 400px; }

  .logo-block {
    position: absolute;
    left: 48px;
    top: 40px;
  }
  .figures-front {
    width: 300px;
    height: 62px;
    border-radius: 4px;
    background: linear-gradient(90deg, var(--figure-dark), var(--figure-light));
  }
  .brand-name {
    display: block;
    font-weight: 600;
    font-size: 40px;
    color: var(--purple);
    line-height: 1.1;
  }
  .logo-block .brand-name { margin-top: 10px; }

  .contact-block {
    position: absolute;
    left: 48px;
    top: 188px;
  }
  .person-name {
    font-size: 26px;
    font-weight: 600;
    color: var(--purple);
  }
  .person-name .credentials {
    font-size: 15px;
    font-weight: 600;
  }
  .person-title {
    font-size: 17px;
    color: var(--ink);
    margin-top: 2px;
    margin-bottom: 14px;
  }
  .contact-list { list-style: none; }
  .contact-item {
    display: flex;
    align-items: center;
    gap: 10px;
    font-size: 15px;
    color: var(--grey);
    line-height: 27px;
  }
  .contact-icon { width: 14px; height: 14px; fill: var(--purple); flex: none; }

  .back-website {
    position: absolute;
    left: 34px;
    top: 0;
    height: 400px;
    writing-mode: vertical-rl;
    transform: rotate(180deg);
    text-align: center;
    font-size: 16px;
    letter-spacing: 4px;
    color: #ffffff;
  }
  .back-logo {
    position: absolute;
    left: 130px;
    top: 100px;
    width: 500px;
    display: flex;
    flex-direction: column;
    align-items: center;
    gap: 14px;
  }
  .figures-back {
    width: 440px;
    height: 120px;
    border-radius: 4px;
    background: linear-gradient(90deg, var(--purple), var(--purple-light));
  }
</style>
</head>
<body>
  <section class="card card-front">
    <svg class="front-swoosh" viewBox="0 0 700 400" aria-hidden="true">
      <rect width="700" height="400" fill="var(--purple)"/>
      <path d="M0 0 H520 C640 60 700 240 700 400 H0 Z" fill="var(--black)"/>
      <path d="M0 0 H420 C590 50 685 220 690 400 H0 Z" fill="var(--card-white)"/>
    </svg>

    <div class="logo-block">
      <div class="figures-front" role="img" aria-label="Row of silhouette figures walking hand in hand, from adult to small child"></div>
      <span class="brand-name">Brightpaths</span>
    </div>

    <div class="contact-block">
      <p class="person-name">Dorota Valk, <span class="credentials">CCC-SLP, TSSLD</span></p>
      <p class="person-title">Bilingual Speech Language Pathologist</p>
      <ul class="contact-list">
        <li class="contact-item">
          <svg class="contact-icon" viewBox="0 0 24 24"><path d="M6.6 10.8a15.1 15.1 0 0 0 6.6 6.6l2.2-2.2a1 1 0 0 1 1-.25 11.4 11.4 0 0 0 3.6.57 1 1 0 0 1 1 1V20a1 1 0 0 1-1 1A17 17 0 0 1 3 4a1 1 0 0 1 1-1h3.5a1 1 0 0 1 1 1c0 1.25.2 2.45.57 3.6a1 1 0 0 1-.25 1z"/></svg>
          (555) 271-8390
        </li>
        <li class="contact-item">
          <svg class="contact-icon" viewBox="0 0 24 24"><path d="M2 5h20v14H2z M2 5l10 8 10-8" fill="none" stroke="var(--purple)" stroke-width="2.4"/></svg>
          dorotavalk@brightpathsslp.example
        </li>
        <li class="contact-item">
          <svg class="contact-icon" viewBox="0 0 24 24"><circle cx="12" cy="12" r="10"/></svg>
          www.Brightpathsslp.example
        </li>
      </ul>
    </div>
  </section>

  <section class="card card-back">
    <p class="back-website">www.Brightpathsslp.example</p>
    <div class="back-logo">
      <div class="figures-back" role="img" aria-label="Row of purple silhouette figures walking hand in hand, from adult to small child"></div>
      <span class="brand-name">Brightpaths</span>
    </div>
  </section>
</body>
</html>
```